Stationery Design Project

Our business in mainly in the Natural Soap and Cosmetics.
Our letter heads, business cards and etc. to be have design on both side.

Target Market(s)

Aged from 21 to 60

Requirements
Must have
• Business card and Letter Head must have a chalkboard design on the back.

```html
<!DOCTYPE html>
<html lang="en">
<head>
<meta charset="utf-8">
<title>Lathery – Business Card Back</title>
<link rel="stylesheet" href="https://fonts.googleapis.com/css2?family=Amatic+SC:wght@700&display=swap">
<style>
  :root {
    --chalkboard-dark: #1f1f1f;
    --chalkboard-mid: #3a3a3a;
    --chalk-white: #f4f2ee;
    --chalk-teal: #7fbcae;
    --chalk-pink: #f1a9a8;
    --illustration-tone-a: rgba(255, 255, 255, 0.16);
    --illustration-tone-b: rgba(241, 169, 168, 0.10);
  }
  html, body {
    margin: 0;
    padding: 0;
    width: 686px;
    height: 1200px;
    overflow: hidden;
    background: var(--chalkboard-dark);
  }
  .card {
    position: relative;
    width: 686px;
    height: 1200px;
    overflow: hidden;
    background:
      radial-gradient(ellipse 70% 55% at 50% 40%, var(--chalkboard-mid) 0%, #2c2c2c 55%, var(--chalkboard-dark) 100%);
    font-family: "Amatic SC", cursive;
    text-align: center;
  }
  .card__illustration {
    position: absolute;
    left: 195px;
    top: 130px;
    width: 296px;
    height: 430px;
  }
  .card__brand {
    position: absolute;
    left: 0;
    right: 0;
    top: 560px;
    margin: 0;
    font-size: 92px;
    font-weight: 700;
    line-height: 1;
    color: var(--chalk-teal);
    letter-spacing: 2px;
  }
  .card__tagline {
    position: absolute;
    left: 0;
    right: 0;
    top: 688px;
    margin: 0;
    font-size: 58px;
    font-weight: 700;
    line-height: 1;
    color: var(--chalk-white);
    letter-spacing: 2px;
  }
  .card__contact {
    position: absolute;
    left: 0;
    right: 0;
    top: 768px;
    margin: 0;
    font-style: normal;
    font-size: 44px;
    font-weight: 700;
    line-height: 41px;
    color: var(--chalk-pink);
    letter-spacing: 2px;
  }
  .card__contact span { display: block; }
</style>
</head>
<body>
  <main class="card">
    <svg class="card__illustration" viewBox="0 0 296 430" role="img" aria-label="Chalk drawing of a clawfoot bathtub with colourful leaves and petals floating above it">
      <defs>
        <radialGradient id="illustrationGlow" cx="50%" cy="55%" r="60%">
          <stop offset="0%" stop-color="var(--illustration-tone-a)"/>
          <stop offset="100%" stop-color="var(--illustration-tone-b)"/>
        </radialGradient>
      </defs>
      <rect x="0" y="0" width="296" height="430" rx="24" fill="url(#illustrationGlow)"/>
    </svg>

    <h1 class="card__brand">lathery</h1>
    <p class="card__tagline">Natural Soap &amp; Cosmetics</p>
    <address class="card__contact">
      <span class="card__name">Firstname Last</span>
      <span class="card__email">info@lathery.com</span>
      <span class="card__phone">1.800.123.4567</span>
    </address>
  </main>
</body>
</html>
```